Life Coaching business needs a new flyer

We are an Australian business that specialises in Life Coaching, Career Coaching, Health and Wellness Coaching, Yoga and Pilates. We need a A4 double sided flyer that is full colour and folded to DL format. I have attached a couple of designs that I like and some pictures and would like the flyer to be bright yet stylish.

Life Coaching

```html
<!DOCTYPE html>
<html lang="en">
<head>
<meta charset="utf-8">
<title>Brightpath Coaching – DL Trifold</title>
<link rel="stylesheet" href="https://fonts.googleapis.com/css2?family=Lora:wght@400;700&display=swap">
<style>
:root{
  --blue:#2b8fcf;
  --blue-deep:#1d6aab;
  --green:#3cae48;
  --white:#ffffff;
  --ink-blue:#1f6fb0;
  --page:#e6e6e6;
  --paper-shade:#f2f2f2;
}
*{box-sizing:border-box;margin:0;padding:0}
html,body{width:1091px;height:1200px;overflow:hidden;background:var(--page)}
body{position:relative;font-family:"Lora",Georgia,serif;font-size:8.4px;line-height:1.38;color:var(--white)}
.sheet{position:absolute;left:145px;width:800px;height:566px;display:flex;box-shadow:0 6px 18px rgba(0,0,0,.18)}
.sheet--outside{top:24px}
.sheet--inside{top:610px}
.panel{position:relative;width:266.67px;height:100%;overflow:hidden}
.panel--blue{background:linear-gradient(170deg,var(--blue) 0%,var(--blue-deep) 100%)}
.panel--white{background:linear-gradient(180deg,var(--white),var(--paper-shade));color:var(--ink-blue)}
.photo{position:absolute;border-radius:50%;border:5px solid var(--white);box-shadow:0 0 0 3px var(--green)}
.band{position:absolute;background:var(--green);color:var(--white);font-weight:400;letter-spacing:.5px;text-transform:uppercase}
h2,h3{font-weight:400}

/* testimonials */
.clients-band{left:0;top:44px;width:240px;height:34px;padding:9px 0 0 30px;font-size:16px;clip-path:polygon(0 0,100% 0,92% 100%,0 100%)}
.quote{position:absolute;left:28px;width:214px;border:2px solid var(--blue);border-top:none;border-right:none;border-radius:0 0 0 10px;padding:6px 20px 6px 22px;font-size:7.8px;color:var(--blue)}
.quote::before,.quote::after{position:absolute;color:var(--green);font-size:26px;font-weight:700;line-height:1}
.quote::before{content:"\201C";left:-4px;top:14px}
.quote::after{content:"\201D";right:-2px;top:-4px}
.quote__name{display:block;color:var(--green);font-size:10.5px;margin-top:2px}
.social{position:absolute;bottom:18px;left:28px;right:20px;display:flex;justify-content:space-between;font-size:10px;color:#333}
.social span{display:flex;align-items:center;gap:5px}
.dot{display:inline-block;width:16px;height:16px;border-radius:50%;background:var(--green)}

/* intro panel */
.intro__title{position:absolute;left:26px;top:40px;width:220px;font-size:17px;line-height:1.2}
.intro__text{position:absolute;left:26px;width:215px}
.contact{position:absolute;left:26px;bottom:26px;font-size:9.5px;line-height:1.7}
.contact div{display:flex;align-items:center;gap:8px}

/* cover */
.cover__brand{position:absolute;top:0;left:0;right:0;height:58px;background:var(--white);display:flex;align-items:center;justify-content:center;gap:8px;color:var(--ink-blue);font-size:14px}
.cover__brand .mark{width:22px;height:22px;border-radius:50%;background:var(--green)}
.services{position:absolute;left:0;right:0;top:382px;display:flex;justify-content:space-around;padding:0 20px;text-align:center;font-size:8px}
.services .thumb{width:44px;height:44px;border-radius:50%;border:3px solid var(--white);box-shadow:0 0 0 2px var(--green);margin:0 auto 6px}
.cover__web{position:absolute;bottom:34px;width:100%;text-align:center;font-size:9.5px}

/* inside left */
.asks{position:absolute;left:24px;top:26px;width:225px;list-style:none}
.asks li{position:relative;padding-left:16px;margin-bottom:3px;font-size:8.6px}
.asks li::before{content:"";position:absolute;left:0;top:2px;width:9px;height:9px;border-radius:50%;background:var(--white)}
.asks li::after{content:"";position:absolute;left:2px;top:4.5px;width:3px;height:3px;border-right:1.3px solid var(--blue);border-top:1.3px solid var(--blue);transform:rotate(45deg)}
.h-caps{font-size:11px;text-transform:uppercase;margin-bottom:3px}
.mission{position:absolute;left:24px;top:142px;width:225px}
.mission p{margin-bottom:8px}
.answer{position:absolute;left:-40px;top:375px;width:350px;height:300px;border-radius:50%;border:6px solid var(--white);box-shadow:0 0 0 3px var(--green);background:linear-gradient(180deg,#5aa9e6 0%,#8ec7ef 45%,#d9a58a 80%,#c05b4b 100%)}
.answer__text{position:absolute;left:40px;top:395px;width:200px;text-align:center;font-size:15px;line-height:1.2}

/* inside middle */
.lc-band{left:60px;top:26px;width:206px;height:24px;background:var(--white);color:var(--green);padding:5px 0 0 34px;font-size:11px}
.lc-thumb{position:absolute;left:28px;top:12px;width:50px;height:50px;border-radius:50%;border:3px solid var(--white);box-shadow:0 0 0 2px var(--green);background:linear-gradient(135deg,#7fb6dc,#c74d3f 60%,#2f5e8f)}
.coaching{position:absolute;left:22px;top:76px;width:228px}
.coaching p{margin-bottom:8px}
.coaching .h-caps{margin-top:4px}

/* inside right */
.help{position:absolute;left:22px;top:22px;width:230px}
.help__title{color:var(--green);font-size:10.5px;text-transform:uppercase;margin-bottom:3px}
.help__lead{color:var(--green);margin:3px 0}
.ticks{list-style:none}
.ticks li{position:relative;padding-left:14px;line-height:1.33}
.ticks li::before{content:"";position:absolute;left:0;top:2px;width:9px;height:9px;border-radius:50%;background:var(--blue)}
.ticks li::after{content:"";position:absolute;left:2.8px;top:3.3px;width:2.5px;height:4.5px;border-right:1.3px solid var(--white);border-bottom:1.3px solid var(--white);transform:rotate(45deg)}
.svc-band{left:60px;width:207px;height:26px;padding:6px 0 0 42px;font-size:11.5px;clip-path:polygon(6% 0,100% 0,100% 100%,0 100%)}
.svc-thumb{position:absolute;left:24px;width:52px;height:52px;border-radius:50%;border:3px solid var(--white);box-shadow:0 0 0 2px var(--green)}
.svc-text{position:absolute;left:22px;width:228px}
</style>
</head>
<body>

<!-- OUTSIDE -->
<section class="sheet sheet--outside">
  <div class="panel panel--white">
    <h2 class="band clients-band">Our Happy Clients</h2>
    <blockquote class="quote" style="top:98px">I have lost 10 kilos and now have the energy to play with my kids. Thanks Anna for your support/guidance and helping me get rid of my limiting beliefs. I feel I can achieve anything now! The sky's the limit.<span class="quote__name">Mia, Mosman</span></blockquote>
    <blockquote class="quote" style="top:196px">Anna has helped to change my life around in all aspects. I would have been lost without her. Thanks Anna for your professionalism, support and guidance.<span class="quote__name">Chloe, Cremorne</span></blockquote>
    <blockquote class="quote" style="top:282px">I was so busy with kids, work, and my husband I lost who I was. Anna has helped me find the person I am again.<span class="quote__name">Emma, Chatswood</span></blockquote>
    <blockquote class="quote" style="top:362px">"I have lost 10 kilos and now have the energy to play with my kids. Thanks Anna for your support/guidance and helping me get rid of my limiting beliefs. I feel I can achieve anything now! The sky's the limit"<span class="quote__name">Mia, Mosman</span></blockquote>
    <div class="social">
      <span><i class="dot"></i>@brightpathcoach</span>
      <span><i class="dot"></i>@brightpathcoach</span>
    </div>
  </div>

  <div class="panel panel--blue">
    <h1 class="intro__title">Brightpath Coaching &amp; Meditation Centre</h1>
    <p class="intro__text" style="top:112px">A professional service that can help you achieve the goals that you are looking for in Life Coaching, Meditation, and Yoga/Pilates.</p>
    <p class="intro__text" style="top:160px">If you are ready to take your life to the next level and would like to know more, please contact us.</p>
    <div class="photo" role="img" aria-label="Photo of a joyful woman raising her arms beside a pink car under a blue sky" style="left:36px;top:222px;width:196px;height:196px;background:linear-gradient(160deg,#8cc4ee 0%,#bfe0f5 40%,#e46c9a 70%,#9a3f66 100%)"></div>
    <div class="contact">
      <div><svg width="12" height="12" viewBox="0 0 24 24"><path fill="#fff" d="M6.6 10.8a15 15 0 0 0 6.6 6.6l2.2-2.2c.3-.3.7-.4 1-.2 1.1.4 2.3.6 3.6.6.6 0 1 .4 1 1V20c0 .6-.4 1-1 1A17 17 0 0 1 3 4c0-.6.4-1 1-1h3.5c.6 0 1 .4 1 1 0 1.3.2 2.5.6 3.6.1.3 0 .7-.2 1z"/></svg>02 9000 4127</div>
      <div><svg width="12" height="10" viewBox="0 0 24 18"><rect x="1" y="1" width="22" height="16" fill="none" stroke="#fff" stroke-width="2"/><path d="M1 1l11 9 11-9" fill="none" stroke="#fff" stroke-width="2"/></svg>hello@brightpathcoaching.com.au</div>
    </div>
  </div>

  <div class="panel panel--blue">
    <div class="cover__brand"><i class="mark"></i>Brightpath Coaching</div>
    <div class="photo" role="img" aria-label="Photo of a cheerful group of young friends laughing together outdoors" style="left:22px;top:80px;width:226px;height:226px;background:linear-gradient(170deg,#f3e0b8 0%,#d9a36f 45%,#b2463f 70%,#3b5f8c 100%)"></div>
    <div class="services">
      <div><div class="thumb" role="img" aria-label="Photo of a signpost with life direction signs" style="background:linear-gradient(135deg,#6fb2e0,#c2493d 60%,#2d5a89)"></div>Life<br>Coaching</div>
      <div><div class="thumb" role="img" aria-label="Photo of two people meditating" style="background:linear-gradient(135deg,#cfe4f4,#8fb5d6 55%,#a268a8)"></div>Meditation</div>
      <div><div class="thumb" role="img" aria-label="Photo of a woman in a yoga pose by the sea" style="background:linear-gradient(135deg,#a9d4f2,#e8f4fb 55%,#5e9ccc)"></div>Yoga/<br>Pilates</div>
    </div>
    <p class="cover__web">www.brightpathcoaching.com.au</p>
  </div>
</section>

<!-- INSIDE -->
<section class="sheet sheet--inside">
  <div class="panel panel--blue">
    <ul class="asks">
      <li>Are you looking at making changes this year?</li>
      <li>Are you stuck in a rut or at a crossroad in your life?</li>
      <li>Are you wanting to lose weight but can't get motivated?</li>
      <li>Do you have ongoing problems with your career, relationships, or just life itself?</li>
    </ul>
    <div class="mission">
      <h3 class="h-caps">Our Mission</h3>
      <p>To help you become the best possible person you can be. Mentally, physically, and spiritually.</p>
      <p>We offer highly qualified and compassionate trainers/coaches for Life Coaching, Meditation, Yoga and Pilates.</p>
      <p>We will guide and motivate you every step of the way to achieve all your dreams and goals.</p>
    </div>
    <div class="answer" role="img" aria-label="Photo of four happy friends jumping against a bright blue sky"></div>
    <p class="answer__text">Life coaching is<br>the answer!</p>
  </div>

  <div class="panel panel--blue">
    <h2 class="band lc-band">Life Coaching</h2>
    <div class="lc-thumb" role="img" aria-label="Photo of a signpost pointing to life, family, career and health"></div>
    <div class="coaching">
      <p>Your Life Coach will give you the confidence and the ability to move forward in a positive manner in all areas of your life where you crave change.</p>
      <p>Life Coaching is about breaking down the barriers preventing this change from happening, and creating the ideal environment for positive action to take place. It is a holistic approach, which looks at the present and sets goals for a totally successful future.</p>
      <h3 class="h-caps">Career Coaching</h3>
      <p>Are you at a crossroads in your career and at a loss about what to do next? Do you want your work to be in alignment with the authentic you? It can be difficult to assess career options, goals, and strategies, and have the confidence to implement changes on your own. With the right coaching support, you will gain the clarity that you need to take control and have a fulfilling and rewarding career.</p>
      <h3 class="h-caps">Wellness Coaching</h3>
      <p>Health and wellness coaches help their clients find the motivation and tools to achieve their health and wellness goals, working with the client to examine and improve the psychological framework that supports those goals.</p>
    </div>
  </div>

  <div class="panel panel--white">
    <div class="help">
      <h3 class="help__title">Why would I need help?</h3>
      <p>Coaching is for anyone who wants to make lasting changes in their life.</p>
      <p class="help__lead">Coaching can assist with such issues as:</p>
      <ul class="ticks">
        <li>Creating a better work- life balance</li>
        <li>Resolving relationship issues</li>
        <li>Career guidance</li>
        <li>Stress management</li>
        <li>Weight loss and fitness</li>
        <li>Motivation and goal setting</li>
        <li>Boosting your self esteem</li>
        <li>Overcoming negative emotions and thoughts</li>
        <li>Better time management</li>
      </ul>
    </div>
    <h3 class="band svc-band" style="top:250px">Meditation</h3>
    <div class="svc-thumb" role="img" aria-label="Photo of two women meditating" style="top:238px;background:linear-gradient(135deg,#d7e9f6,#8fb5d6 55%,#a268a8)"></div>
    <p class="svc-text" style="top:300px">We specialise in teaching meditation from beginners to advanced and teach a variety of techniques for stress reduction, peace of mind, stillness, and clarity.</p>
    <h3 class="band svc-band" style="top:372px">Yoga/Pilates</h3>
    <div class="svc-thumb" role="img" aria-label="Photo of a woman holding a yoga pose by the ocean" style="top:360px;background:linear-gradient(135deg,#a9d4f2,#eef7fc 55%,#5e9ccc)"></div>
    <p class="svc-text" style="top:424px">Your highly qualified and experienced Yoga or Pilates instructor will come to you and create a fun and varied workout based on what you enjoy and what your goals are.</p>
  </div>
</section>

</body>
</html>
```